Plexlink Banners for a Joint Supplement

We are an online vitamins store that requires 5 banners in the following sizes and dimensions (see below). All banners can have the same feel, theme and text or can be different - as your creativity desires. Since these are going to be used on zorbixs ad content network, they MUST abide by Zorbix's terms (see below). Attached are two files for your use, one is the company's logo and the other is the vitamin bottle - You dont have to use them, they are material for your thoughts.

Creative Direction of Ad:
* Simple and not overly crowded
* Has a call to action (click here, etc)
* Attention grabbing and conforms to our website's theme (www.tessalinhealth.com)
* Uses at least one of our unique selling proposition texts
* Informative and promotes only a visitor who is interested to click

Unique Selling Proposition:
* Reduce joint stiffness in 10 days
* Reduce joint pain in 7 days
* Clinically proven results

Zorbix Terms:
Ad images must be clear, recognizable, and relevant. Text appearing in the ad images must be legible. We reserve the right to disapprove low quality or blurry ad images.

Strobing, flashing backgrounds, or otherwise distracting ads are not allowed.
Your ads cannot mimic news articles and features. They may also not contain screenshots of Zorbix PlexLinks text ads or otherwise simulate an PlexLinks text ad in any way.
Ads cannot pretend to be a system or site warning.
Ads cannot mimic or resemble Ferrolite, Quon, or Vemo dialogue boxes, error message, etc.
Ads cannot have mock animated features or icons.
Ads can have an imaged button as long as the purpose of the message within the button is served or achieved through the landing page.
Specific for animated and display ad builder (template) ads:
Ads cannot have mock animated features or icons without the functionality working.

Sizes: (MAX 50K or smaller)
1. Square 250 x 239
2. Small Square 200 x 189
3. Leaderboard 728 x 79
4. Medium Rectangle 300 x 239
5. Large Rectangle 336 x 269

Winner will send the files in .Gif, JPEG, & PSD. If you have any questions, please dont hesitate to ask.

Project Deadline Extended
Reason: I was out of town and had not have a chance to review the submissions and provide feedback for adjustments. All the feedback will be provided by Monday 3rd for the last round.

Thanks

Target Market(s)

Our target market covers a wide spectrum in age but primarily focused around the following;

Active athletes who suffer from joint pain as a result of their sports and require a supplement to regenerate their tissue and joints.

Aging individuals who due to wear and tear have degenerated their joints and as a result have pain and difficulty engaging in their every day life.

Industry/Entity Type

Store

Requirements
Should not have
• Image quality

Strobing and flashing

Mimicking news articles or text ads

Trick to click

```html
<!DOCTYPE html>
<html lang="en">
<head>
<meta charset="utf-8">
<title>Tessalin Health – Joint Pain Banner</title>
<link href="https://fonts.googleapis.com/css2?family=Questrial&display=swap" rel="stylesheet">
<style>
  :root {
    --page-bg: #f1f1f1;
    --banner-bg: #fbfbfb;
    --banner-shade: #ececec;
    --banner-edge: #d6d6d6;
    --brand-cyan: #29c4e0;
    --brand-muted: #9fb8c2;
    --copy-grey: #6f7376;
    --bottle-teal: #1d8ea0;
    --bottle-white: #eef2f3;
    --bottle-navy: #1f3d52;
  }
  * { margin: 0; padding: 0; box-sizing: border-box; }
  html, body {
    width: 1200px;
    height: 900px;
    overflow: hidden;
    background: var(--page-bg);
    font-family: "Questrial", sans-serif;
  }
  .ad-banner {
    position: absolute;
    left: 33px;
    top: 0;
    width: 1134px;
    height: 900px;
    background: linear-gradient(160deg, var(--banner-bg) 0%, #ffffff 45%, var(--banner-shade) 100%);
    border: 2px solid var(--banner-edge);
    overflow: hidden;
  }
  .brand-name {
    position: absolute;
    left: 78px;
    top: 235px;
    font-size: 54px;
    color: var(--brand-muted);
    letter-spacing: 0.5px;
  }
  .headline {
    position: absolute;
    left: 70px;
    top: 375px;
    font-size: 112px;
    color: var(--brand-cyan);
    font-weight: 400;
    letter-spacing: -1px;
  }
  .call-to-action {
    position: absolute;
    left: 78px;
    top: 545px;
    font-size: 66px;
    line-height: 80px;
    color: var(--copy-grey);
  }
  .product-bottle {
    position: absolute;
    left: 640px;
    top: 20px;
    width: 470px;
    height: 860px;
  }
</style>
</head>
<body>
  <main class="ad-banner">
    <div class="brand-name">tessalinhealth</div>
    <h1 class="headline">Joint pain?</h1>
    <p class="call-to-action">Click here<br>for Clinically<br>proven results</p>
    <svg class="product-bottle" viewBox="0 0 470 860" role="img" aria-label="Jointara supplement bottle with teal cap and dark blue label">
      <defs>
        <linearGradient id="bottleBody" x1="0" x2="1" y1="0" y2="0">
          <stop offset="0" stop-color="#d9e0e2"/>
          <stop offset="0.4" stop-color="var(--bottle-white)"/>
          <stop offset="1" stop-color="#c9d2d5"/>
        </linearGradient>
        <linearGradient id="bottleCap" x1="0" x2="1">
          <stop offset="0" stop-color="#157c8c"/>
          <stop offset="0.45" stop-color="#3fb6c6"/>
          <stop offset="1" stop-color="#12707f"/>
        </linearGradient>
        <linearGradient id="bottleLabel" x1="0" x2="1">
          <stop offset="0" stop-color="var(--bottle-teal)"/>
          <stop offset="0.5" stop-color="var(--bottle-navy)"/>
          <stop offset="1" stop-color="#173246"/>
        </linearGradient>
      </defs>
      <rect x="40" y="0" width="390" height="150" rx="30" fill="url(#bottleCap)"/>
      <rect x="60" y="150" width="350" height="70" fill="url(#bottleBody)"/>
      <rect x="10" y="220" width="450" height="620" rx="50" fill="url(#bottleBody)"/>
      <rect x="10" y="300" width="450" height="470" fill="url(#bottleLabel)"/>
    </svg>
  </main>
</body>
</html>
```